Postcard Design

A house cleaning business. Focus on time saving and stress free. Free estimates. Want it to state that we can make your home sparkle or shine. I have been using the colors purple and black in the logo which I will attach.

Reason: I need a few more days to decide on this. Thank you

Industry/Entity Type

House

Colors
886aae
6b449b

Requirements
Must have
• website www.marlowbrookcare.us
phone # 607-391-2858

```html
<!DOCTYPE html>
<html lang="en">
<head>
<meta charset="utf-8">
<title>Marlow Brook Cleaning Company – Postcard</title>
<link rel="stylesheet" href="https://fonts.googleapis.com/css2?family=Hind:wght@300;400;500;600;700&family=Kaushan+Script&display=swap">
<style>
  :root {
    --purple: #6b449b;
    --purple-light: #886aae;
    --ink: #1d1d1f;
    --grey-text: #3a3a3a;
    --rule: #c9c9c9;
    --paper: #ffffff;
    --backdrop: #e9e7e4;
  }
  * { box-sizing: border-box; margin: 0; padding: 0; }
  html, body { width: 1200px; height: 1000px; overflow: hidden; }
  body {
    position: relative;
    background: var(--backdrop);
    font-family: "Hind", sans-serif;
    color: var(--ink);
  }

  /* ---------- Front ---------- */
  .card-front {
    position: absolute;
    left: 95px; top: 52px;
    width: 558px; height: 430px;
    overflow: hidden;
    box-shadow: 0 6px 18px rgba(0,0,0,.25);
  }
  .front-photo {
    position: absolute; inset: 0;
    background:
      radial-gradient(ellipse 38% 50% at 62% 62%, #e9b8a4 0%, rgba(233,184,164,0) 70%),
      radial-gradient(ellipse 30% 25% at 55% 78%, #e0507a 0%, rgba(224,80,122,0) 75%),
      linear-gradient(180deg, #eeeef1 0%, #dcdbe2 55%, #c9c7d0 100%);
  }
  .front-brand {
    position: absolute;
    left: 16px; top: 110px;
    width: 180px;
    font-weight: 600;
    font-size: 24px;
    line-height: 1.05;
    color: var(--purple);
  }
  .front-brand .brand-dot {
    display: block;
    width: 26px; height: 26px;
    border-radius: 50%;
    background: var(--purple);
    margin-bottom: 8px;
  }
  .headline-script {
    position: absolute;
    left: 186px; top: 42px;
    font-family: "Kaushan Script", cursive;
    font-size: 34px;
    color: var(--purple);
  }
  .headline-bold {
    position: absolute;
    left: 220px; top: 88px;
    font-weight: 700;
    font-size: 31px;
    letter-spacing: 1px;
    color: var(--purple);
  }
  .cta-band {
    position: absolute;
    left: 19px; top: 318px;
    width: 514px; height: 88px;
    background: var(--purple);
    color: #fff;
    box-shadow: 0 6px 10px rgba(0,0,0,.25);
  }
  .cta-call {
    position: absolute;
    left: 26px; top: 14px;
    font-weight: 300;
    font-size: 28px;
    line-height: 1;
    letter-spacing: .3px;
  }
  .cta-free {
    position: absolute;
    left: 26px; top: 46px;
    font-weight: 700;
    font-size: 29px;
    line-height: 1;
    letter-spacing: .3px;
  }
  .cta-phone {
    position: absolute;
    left: 264px; top: 16px;
    display: flex; align-items: center; gap: 8px;
    font-weight: 600;
    font-size: 30px;
    line-height: 1;
  }
  .cta-phone svg { width: 24px; height: 24px; }
  .cta-web {
    position: absolute;
    left: 268px; top: 56px;
    font-size: 15px;
    letter-spacing: .4px;
  }

  /* ---------- Back ---------- */
  .card-back {
    position: absolute;
    left: 502px; top: 507px;
    width: 554px; height: 428px;
    background: var(--paper);
    box-shadow: 0 6px 18px rgba(0,0,0,.25);
  }
  .back-brand {
    position: absolute;
    left: 18px; top: 40px;
    width: 160px;
    font-weight: 600;
    font-size: 22px;
    line-height: 1.05;
    color: var(--purple);
  }
  .back-brand .brand-dot {
    display: block;
    width: 24px; height: 24px;
    border-radius: 50%;
    background: var(--purple);
    margin-bottom: 8px;
  }
  .contact-list {
    position: absolute;
    left: 184px; top: 42px;
    list-style: none;
  }
  .contact-list li {
    display: flex; align-items: center; gap: 8px;
    height: 23px;
    font-weight: 600;
    color: var(--ink);
  }
  .contact-list .c-phone { font-size: 16px; }
  .contact-list .c-small { font-size: 11.5px; letter-spacing: .2px; }
  .contact-list svg { width: 13px; height: 13px; flex: none; }
  .stamp-box {
    position: absolute;
    left: 430px; top: 13px;
    width: 100px; height: 117px;
    border: 2px solid #e3e3e3;
  }
  .back-copy {
    position: absolute;
    left: 20px; top: 194px;
    width: 236px;
    text-align: center;
    font-size: 16.5px;
    line-height: 25px;
    color: var(--grey-text);
  }
  .back-copy p + p { margin-top: 8px; }
  .address-lines {
    position: absolute;
    left: 284px; top: 195px;
    width: 240px;
  }
  .address-lines span {
    display: block;
    height: 1px;
    background: var(--rule);
    margin-bottom: 33px;
  }
</style>
</head>
<body>

  <section class="card-front">
    <div class="front-photo" role="img" aria-label="Photo of a smiling cleaner in a pink shirt and red gloves holding a spray bottle and a blue cloth in a bright living room"></div>

    <div class="front-brand"><span class="brand-dot"></span>Marlow Brook Cleaning Company</div>

    <div class="headline-script">A sparking shine,</div>
    <div class="headline-bold">EVERY TIME.</div>

    <div class="cta-band">
      <div class="cta-call">CALL US FOR A</div>
      <div class="cta-free">FREE ESTIMATE</div>
      <div class="cta-phone">
        <svg viewBox="0 0 24 24" aria-hidden="true"><path fill="#fff" d="M6.6 10.8c1.4 2.8 3.8 5.1 6.6 6.6l2.2-2.2c.3-.3.7-.4 1-.2 1.1.4 2.3.6 3.6.6.6 0 1 .4 1 1V20c0 .6-.4 1-1 1C10.6 21 3 13.4 3 4c0-.6.4-1 1-1h3.5c.6 0 1 .4 1 1 0 1.3.2 2.5.6 3.6.1.3 0 .7-.2 1z"/></svg>
        607-391-2858
      </div>
      <div class="cta-web">WWW.MARLOWBROOKCARE.US</div>
    </div>
  </section>

  <section class="card-back">
    <div class="back-brand"><span class="brand-dot"></span>Marlow Brook Cleaning Company</div>

    <ul class="contact-list">
      <li class="c-phone">
        <svg viewBox="0 0 24 24" aria-hidden="true"><path fill="#6b449b" d="M6.6 10.8c1.4 2.8 3.8 5.1 6.6 6.6l2.2-2.2c.3-.3.7-.4 1-.2 1.1.4 2.3.6 3.6.6.6 0 1 .4 1 1V20c0 .6-.4 1-1 1C10.6 21 3 13.4 3 4c0-.6.4-1 1-1h3.5c.6 0 1 .4 1 1 0 1.3.2 2.5.6 3.6.1.3 0 .7-.2 1z"/></svg>
        607-391-2858
      </li>
      <li class="c-small">
        <svg viewBox="0 0 24 24" aria-hidden="true"><circle cx="12" cy="12" r="10" fill="none" stroke="#6b449b" stroke-width="2.4"/><ellipse cx="12" cy="12" rx="4.5" ry="10" fill="none" stroke="#6b449b" stroke-width="2"/><line x1="2" y1="12" x2="22" y2="12" stroke="#6b449b" stroke-width="2"/></svg>
        WWW.MARLOWBROOKCLEANING.US
      </li>
      <li class="c-small">
        <svg viewBox="0 0 24 24" aria-hidden="true"><circle cx="12" cy="12" r="4" fill="none" stroke="#6b449b" stroke-width="2.6"/><path d="M16 8v5.5c0 1.7 2.5 2.3 3.6.6A9 9 0 1 0 16 20" fill="none" stroke="#6b449b" stroke-width="2.6" stroke-linecap="round"/></svg>
        MARLOWBROOK33@MAILBOX.US
      </li>
    </ul>

    <div class="stamp-box"></div>

    <div class="back-copy">
      <p>Marlow Brook cleaning company offers high-quality home cleaning services.</p>
      <p>Our professionals are insured and bonded.</p>
    </div>

    <div class="address-lines">
      <span></span><span></span><span></span><span></span><span></span>
    </div>
  </section>

</body>
</html>
```